Business Card design for a skin clinic

i would like a business card design for our skin clinic.
our logo colors are Blue and Grey and Bule /white.
we are searching for a minimalistic design yet very elegant,dynamic and professional which can reflect a professional medical skin care clinic( not a beauty salon).
THE DESGIN IS NOT FOR A PERSON IT WILL BE USED IN THE CLINIC FOR CLIENTS SO THERE SHOULD BE NO NAME OF A PERSON ONLY THE CLINIC NAME AND THE CONTACT INFO

Target Market(s)
young and old womens
Industry/Entity Type
Business
Contact Information for Business Card
we have 2 address and both should be on the card.
address A: Lindenhoflaan 214B, 3041KP Rotterdam, Tel 010 483 21 95
address B: Zonnewijzerstraat 238, 1062RT Amsterdam Tel 020 571 3829
website www.huidpuntzorg.nu, email info@huidpuntzorg.nu
Look and feel
Each slider illustrates characteristics of the customer's brand and the style your logo design should communicate.

```html
<!DOCTYPE html>
<html lang="nl">
<head>
<meta charset="utf-8">
<title>Huidpunt Zorg – visitekaartje</title>
<link href="https://fonts.googleapis.com/css2?family=Open+Sans:wght@400;600;700&display=swap" rel="stylesheet">
<style>
  :root {
    --page-bg: #ecebe9;
    --card-bg: #ffffff;
    --brand-blue: #3a8ccc;
    --brand-grey: #5b5b5e;
    --text-dark: #3f3f42;
    --divider: #8a8a8d;
    --card-shadow: rgba(0, 0, 0, 0.18);
  }
  * { margin: 0; padding: 0; box-sizing: border-box; }
  html, body {
    width: 1200px;
    height: 1000px;
    overflow: hidden;
    background: var(--page-bg);
    font-family: "Open Sans", Arial, sans-serif;
  }
  .canvas { position: relative; width: 1200px; height: 1000px; }

  .card {
    position: absolute;
    left: 266px;
    width: 666px;
    height: 397px;
    background: var(--card-bg);
    box-shadow: 0 4px 14px var(--card-shadow);
  }
  .card--front { top: 74px; }
  .card--back  { top: 533px; }

  /* Front */
  .front-brand {
    position: absolute;
    left: 0; right: 0;
    top: 98px;
    text-align: center;
  }
  .brand-square {
    display: block;
    width: 46px;
    height: 46px;
    margin: 0 auto 38px;
    background: var(--brand-blue);
  }
  .brand-name {
    font-weight: 600;
    color: var(--brand-blue);
    letter-spacing: 3px;
    white-space: nowrap;
  }
  .front-brand .brand-name { font-size: 42px; line-height: 1; }
  .tagline {
    color: var(--brand-grey);
    letter-spacing: 2px;
    white-space: nowrap;
  }
  .front-brand .tagline { font-size: 18px; margin-top: 22px; }

  /* Back */
  .back-brand {
    position: absolute;
    left: 20px;
    width: 302px;
    top: 198px;
    text-align: center;
  }
  .back-brand .brand-name { font-size: 29px; line-height: 1; letter-spacing: 2px; }
  .back-brand .tagline { font-size: 13px; margin-top: 16px; letter-spacing: 1.4px; }

  .divider {
    position: absolute;
    left: 339px;
    top: 77px;
    width: 1px;
    height: 241px;
    background: var(--divider);
  }

  .contact {
    position: absolute;
    left: 372px;
    top: 72px;
    width: 280px;
    color: var(--text-dark);
    font-size: 15.5px;
    line-height: 21px;
  }
  .contact__title {
    font-size: 20px;
    font-weight: 700;
    color: var(--brand-blue);
    letter-spacing: 0.3px;
    margin-bottom: 16px;
  }
  .contact__address { margin-bottom: 4px; }
  .contact__line {
    display: flex;
    align-items: center;
    gap: 6px;
    white-space: nowrap;
  }
  .contact__line svg { flex: none; }
  .location { margin-bottom: 14px; }
  .contact__line + .contact__line { margin-top: 5px; }
</style>
</head>
<body>
<main class="canvas">

  <section class="card card--front" aria-label="Voorkant visitekaartje">
    <div class="front-brand">
      <span class="brand-square" aria-hidden="true"></span>
      <div class="brand-name">HUIDPUNTZORG</div>
      <div class="tagline">next generation skin care</div>
    </div>
  </section>

  <section class="card card--back" aria-label="Achterkant visitekaartje">
    <div class="back-brand">
      <div class="brand-name">HUIDPUNTZORG</div>
      <div class="tagline">next generation skin care</div>
    </div>

    <div class="divider" aria-hidden="true"></div>

    <div class="contact">
      <h2 class="contact__title">HUIDPUNT ZORG</h2>

      <div class="location">
        <p class="contact__address">Lindenhoflaan 214B, 3041KP<br>Rotterdam</p>
        <p class="contact__line">
          <svg width="14" height="12" viewBox="0 0 14 12" aria-hidden="true"><path fill="var(--brand-blue)" d="M1 4 C1 1 13 1 13 4 L10 5 L10 3.5 L4 3.5 L4 5 Z M3 6 L11 6 L12.5 11 L1.5 11 Z"/></svg>
          010 483 21 95
        </p>
      </div>

      <div class="location">
        <p class="contact__address">Zonnewijzerstraat 238, 1062RT<br>Amsterdam</p>
        <p class="contact__line">
          <svg width="14" height="12" viewBox="0 0 14 12" aria-hidden="true"><path fill="var(--brand-blue)" d="M1 4 C1 1 13 1 13 4 L10 5 L10 3.5 L4 3.5 L4 5 Z M3 6 L11 6 L12.5 11 L1.5 11 Z"/></svg>
          020 571 3829
        </p>
      </div>

      <p class="contact__line">
        <svg width="14" height="11" viewBox="0 0 14 11" aria-hidden="true"><rect x="0.5" y="1" width="13" height="9" fill="var(--brand-blue)"/><path d="M1 1.5 L7 6 L13 1.5" stroke="#fff" stroke-width="1.2" fill="none"/></svg>
        info@huidpuntzorg.nu
      </p>
      <p class="contact__line">
        <svg width="15" height="15" viewBox="0 0 15 15" aria-hidden="true"><circle cx="7" cy="7" r="6" fill="var(--brand-blue)"/><path d="M1 7 H13 M7 1 C4 4 4 10 7 13 M7 1 C10 4 10 10 7 13" stroke="#fff" stroke-width="0.9" fill="none"/></svg>
        www.huidpuntzorg.nu
      </p>
    </div>
  </section>

</main>
</body>
</html>
```